CV for an Urgent Care Trade Association Executive search candidate in need of competitive CV refresh

I need a CV refresh to be able to show marketability and skill in a competitive Executive search. I would like to see designs that highlight my skill and ability to hopefully put me in the front running for position.

Industry/Entity Type

Medical/Urgent Care

Requirements
Must have
• CV template
Nice to have
• Nice to have a CV template to be able to add my personal info into

```html
<!DOCTYPE html>
<html lang="en">
<head>
<meta charset="utf-8">
<title>Corwin Delacourt — CV</title>
<link href="https://fonts.googleapis.com/css2?family=Lato:ital,wght@0,300;0,400;0,700;0,900;1,400&display=swap" rel="stylesheet">
<style>
:root{
  --navy:#2a3a4e;
  --gold:#d8bd8e;
  --ink:#2b2b2b;
  --muted:#555;
  --rule:#9a9a9a;
  --paper:#ffffff;
  --backdrop:#ececec;
}
*{box-sizing:border-box;margin:0;padding:0}
html,body{width:1200px;height:801px;overflow:hidden}
body{background:var(--backdrop);font-family:'Lato',sans-serif;color:var(--ink);position:relative}
.page{position:absolute;left:294px;top:12px;width:580px;height:789px;background:var(--paper);overflow:hidden}
.header{position:absolute;left:0;top:0;width:580px;height:163px;background:var(--navy)}
.name-row{position:absolute;left:0;right:26px;top:30px;display:flex;align-items:center;gap:14px}
.name-bar{flex:1;height:6px;background:var(--gold)}
.name{flex:none;white-space:nowrap;color:var(--gold);font-size:31px;letter-spacing:.3px;line-height:1}
.name b{font-weight:900}
.name span{font-weight:400}
.title{position:absolute;left:0;right:0;top:90px;text-align:center;color:var(--gold);font-size:9.5px;letter-spacing:1.6px}
.social{position:absolute;top:130px;display:flex;gap:6px;align-items:center}
.social .mark{width:15px;height:15px;border-radius:3px;background:var(--gold)}
.social p{font-size:8px;color:var(--gold);line-height:1.25}
.summary{position:absolute;left:38px;top:188px;width:474px;height:81px;border:2px solid var(--rule);padding:8px 12px;text-align:center;font-size:7.6px;line-height:12.6px;color:var(--muted)}
.divider{position:absolute;left:199px;top:293px;width:1.5px;height:451px;background:var(--rule)}
.sidebar{position:absolute;left:40px;top:294px;width:145px}
.main{position:absolute;left:228px;top:294px;width:290px}
h2{font-size:11.5px;font-weight:400;letter-spacing:2px;color:var(--ink);margin-bottom:12px}
.award{margin-bottom:9px}
.award .date,.award .note{font-style:italic;font-size:6.6px;color:var(--muted)}
.award h3{font-size:8px;font-weight:400;margin:5px 0 3px;letter-spacing:.2px;white-space:nowrap}
.short-rule{width:66px;height:1px;background:var(--rule);margin:8px 0 10px}
.reference{margin-top:16px}
.ref h3{font-size:7.8px;font-weight:700;margin-bottom:4px}
.ref p{font-size:6.8px;color:var(--muted);line-height:10px}
.ref .contact{display:flex;align-items:center;gap:6px;font-size:7.6px;letter-spacing:.4px;margin-top:3px;color:var(--ink);white-space:nowrap}
.ref .contact svg{width:7px;height:7px;fill:var(--ink);flex:none}
.job{margin-bottom:16px}
.job h3{font-size:7.8px;font-weight:400;margin-bottom:6px}
.job .meta{display:flex;justify-content:space-between;font-size:7px;margin-bottom:8px}
.job .meta em{font-style:italic;color:var(--muted)}
.job .meta span{padding-right:24px}
.job p{font-size:6.9px;line-height:12.6px;color:var(--muted);margin-bottom:6px}
.job ul{list-style:none;padding-left:32px}
.job li{position:relative;font-size:6.9px;line-height:12.6px;color:var(--muted);margin-bottom:6px}
.job li::before{content:"";position:absolute;left:-16px;top:4px;width:4px;height:4px;border-radius:50%;background:var(--ink)}
</style>
</head>
<body>
<div class="page">
  <header class="header">
    <div class="name-row">
      <div class="name-bar"></div>
      <h1 class="name"><b>CORWIN</b> <span>DELACOURT</span></h1>
      <div class="name-bar"></div>
    </div>
    <div class="title">PROFESSIONAL TITLE</div>
    <div class="social" style="left:48px"><div class="mark"></div><p>Chatline<br>/Corwin Delacourt</p></div>
    <div class="social" style="left:168px"><div class="mark"></div><p>ProNetwork<br>/Corwin Delacourt</p></div>
    <div class="social" style="left:290px"><div class="mark"></div><p>Shotboard<br>/Corwin Delacourt</p></div>
    <div class="social" style="left:412px"><div class="mark"></div><p>Folioroom<br>/Corwin Delacourt</p></div>
  </header>

  <section class="summary">When composing your personal profile, divide your information into three sections: who you are, what you can give the firm, and your professional objectives. Utilize it as an opportunity to briefly market yourself and demonstrate that you possess the required abilities and passion for succeeding in the position. Use specific percentages and numbers to quantify accomplishments since this can considerably enhance credibility. This paragraph will be the initial impression you make with recruiters. Therefore, it is essential to keep it brief and straightforward.</section>

  <div class="divider"></div>

  <aside class="sidebar">
    <h2>AWARDS</h2>
    <div class="award"><div class="date">April 2020 1st Position</div><h3>UI/UX DESIGN AWARDS</h3><div class="note">Best UI/UX Designer - 2020</div></div>
    <div class="short-rule"></div>
    <div class="award"><div class="date">May 2021 2nd Position</div><h3>WEB DEVELOPMENT AWARD</h3><div class="note">Wb Development of the Year - 2021</div></div>
    <div class="short-rule"></div>
    <div class="award"><div class="date">January 2022 1st Position</div><h3>SWISS WEB DESIGN AWARD</h3><div class="note">Wb Design of the Year - 2022</div></div>
    <div class="short-rule"></div>
    <div class="award"><div class="date">April 2022 1st Position</div><h3>FOLIOROOM CREATOR AWARD</h3><div class="note">Popular Creator - 2022</div></div>
    <div class="short-rule"></div>

    <section class="reference">
      <h2>REFERENCE</h2>
      <div class="ref">
        <h3>Daniel Mercer</h3>
        <p>Director<br>Northgate Health Partners Ltd.</p>
        <div class="contact"><svg viewBox="0 0 10 10"><path d="M2 0.5 L4 2.8 L3 4 Q4.3 6 6 7 L7.2 6 L9.5 8 L8.3 9.5 Q3.5 9 0.5 1.7 Z"/></svg>+62 811 2040 3319</div>
        <div class="contact"><svg viewBox="0 0 10 10"><path d="M0 2 H10 V8.5 H0 Z M0.8 2.6 L5 5.6 L9.2 2.6" stroke="#fff" stroke-width=".8"/></svg>danielmercer@mailpost.com</div>
      </div>
      <div class="short-rule"></div>
      <div class="ref">
        <h3>Lucas Brenner</h3>
        <p>Director<br>Northgate Health Partners Ltd.</p>
        <div class="contact"><svg viewBox="0 0 10 10"><path d="M2 0.5 L4 2.8 L3 4 Q4.3 6 6 7 L7.2 6 L9.5 8 L8.3 9.5 Q3.5 9 0.5 1.7 Z"/></svg>+62 811 2040 3319</div>
        <div class="contact"><svg viewBox="0 0 10 10"><path d="M0 2 H10 V8.5 H0 Z M0.8 2.6 L5 5.6 L9.2 2.6" stroke="#fff" stroke-width=".8"/></svg>lucasbrenner@mailpost.com</div>
      </div>
    </section>
  </aside>

  <main class="main">
    <h2>WORK EXPERIENCE CONTINUED</h2>
    <article class="job">
      <h3>YOUR POSITION TITLE</h3>
      <div class="meta"><em>Company Name / California</em><span>2012 – 2015</span></div>
      <p>In this part, please provide a description of your professional experience. Describe the successes you've had at work and the breadth of the duties that come with your current position. For example:</p>
      <ul>
        <li>When describing each position, make sure to include at least three and preferably four bullet points, and try to keep the length of each description to a maximum of two lines.</li>
        <li>Your achievements, presented in a grammatically accurate manner, will leave an impression on them. Describe your experiences while putting an emphasis on the skills you've gained and the tangible successes you've achieved.</li>
        <li>When describing each position, make sure to include at least three and preferably four bullet points, and try to keep the length of each description to a maximum of two lines.</li>
      </ul>
    </article>
    <article class="job">
      <h3>YOUR POSITION TITLE</h3>
      <div class="meta"><em>Company Name / California</em><span>2012 – 2015</span></div>
      <p>In this part, please provide a description of your professional experience. Describe the successes you've had at work and the breadth of the duties that come with your current position. For example:</p>
      <ul>
        <li>When describing each position, make sure to include at least three and preferably four bullet points, and try to keep the length of each description to a maximum of two lines.</li>
        <li>Your achievements, presented in a grammatically accurate manner, will leave an impression on them. Describe your experiences while putting an emphasis on the skills you've gained and the tangible successes you've achieved.</li>
      </ul>
    </article>
  </main>
</div>
</body>
</html>
```